Kernwichtel sucht neue Visitenkarten & Briefpapier
Zielgruppe
Wir sind ein Start-Up das unter kernwichtel-beispiel.de ab 2014, deutschlandweit gesunde und frische Früchte zu Ihnen nach Hause oder an den Arbeitsplatz als Abo (wöchentlich/monatlich) per Post liefern möchte. Es sollten später auch Filialen in Deutschland eröffnet werden.
Aufgabenstellung
Entwicklung einer ansprechenden Visitenkarte und Briefpapier. Gestalterische Basis hierfür ist unser Logo. Das Logo kann gerade, oder gedreht werden. Das Briefpapier dient als Rechnung/Lieferschein und Korrespondenz unserer Firma. Das Briefpapier ist 1-Seitig. Die Visitenkarte ist ebenfalls 1-Seitig und auf Deutsch.
Das Design soll "das gewisse Etwas haben" und nicht zu verspielt sein.

```html
<!DOCTYPE html>
<html lang="de">
<head>
<meta charset="utf-8">
<title>Kernwichtel – Briefpapier &amp; Visitenkarten</title>
<link href="https://fonts.googleapis.com/css2?family=Open+Sans:wght@400;600;700&display=swap" rel="stylesheet">
<style>
  :root {
    --orange: #e07a1e;
    --green: #5aad33;
    --ink: #222222;
    --paper: #ffffff;
    --stage: #ffffff;
    --fold: #f0b98a;
  }
  * { box-sizing: border-box; margin: 0; padding: 0; }
  html, body { width: 1200px; height: 1200px; overflow: hidden; background: var(--stage); }
  body { position: relative; font-family: "Open Sans", Arial, sans-serif; color: var(--ink); }

  /* Letterhead */
  .letterhead {
    position: absolute; left: 120px; top: 43px; width: 787px; height: 1114px;
    background: linear-gradient(to bottom, var(--orange) 0 50%, var(--green) 50% 100%);
    box-shadow: 0 0 6px rgba(0,0,0,.12);
  }
  .letterhead-body {
    position: absolute; left: 0; right: 0; top: 19px; bottom: 32px;
    background: var(--paper); border-radius: 30px;
  }
  .fold-mark { position: absolute; left: 0; height: 1px; background: var(--fold); }
  .fold-mark.upper { top: 375px; width: 14px; }
  .fold-mark.lower { top: 538px; width: 22px; }
  .letterhead .brand { position: absolute; right: 32px; top: 118px; }
  .sender-line { position: absolute; left: 75px; top: 168px; font-size: 7.5px; }
  .letter-footer {
    position: absolute; left: 75px; top: 1021px;
    font-size: 9.6px; line-height: 14px; white-space: nowrap;
  }

  /* Brand name set in plain type */
  .brand {
    display: flex; align-items: center; gap: 6px;
    color: var(--orange); font-weight: 700; white-space: nowrap;
  }
  .brand-dot { border-radius: 50%; background: var(--orange); flex: none; }

  /* Business cards */
  .card {
    position: absolute; width: 320px; height: 204px; border-radius: 16px;
    box-shadow: 0 2px 6px rgba(0,0,0,.15);
  }
  .card.front { left: 768px; top: 443px; background: var(--orange); }
  .card.back { left: 837px; top: 733px; background: var(--green); }
  .card-face {
    position: absolute; left: 0; right: 0; top: 6px; bottom: 7px;
    background: var(--paper); border-radius: 16px;
  }
  .card.front .brand {
    position: absolute; left: 0; right: 0; top: 108px; justify-content: center;
    font-size: 21px;
  }
  .card.back .brand { position: absolute; right: 24px; top: 54px; font-size: 11px; }
  .contact-name { position: absolute; left: 21px; top: 78px; font-size: 11px; font-weight: 700; }
  .contact-title { position: absolute; left: 21px; top: 96px; font-size: 7.5px; }
  .contact-address {
    position: absolute; left: 21px; top: 123px; font-size: 9.5px; line-height: 13.5px;
  }
  .contact-lines {
    position: absolute; left: 168px; top: 123px; font-size: 9.5px; line-height: 13.5px;
    border-collapse: collapse;
  }
  .contact-lines td { padding: 0; white-space: nowrap; }
  .contact-lines td:first-child { width: 36px; }
  .contact-mail { position: absolute; left: 168px; top: 171px; font-size: 9.5px; }
</style>
</head>
<body>

<section class="letterhead" aria-label="Briefpapier">
  <div class="letterhead-body">
    <span class="fold-mark upper"></span>
    <span class="fold-mark lower"></span>
    <div class="brand" style="font-size:18px;">
      <span class="brand-dot" style="width:12px;height:12px;"></span>kernwichtel-beispiel.de
    </div>
    <p class="sender-line">Musterfirma · Musterstrasse 123 · 12345 Musterhausen</p>
    <div class="letter-footer">
      <p>Musterfirma | Musterstraße | 12345 Musterhausen | Telefon &nbsp;+49 (0) 1234 567890 &nbsp;| Fax +49 (0) 1234 567891 | E-Mail: info@kernwichtel-beispiel.de</p>
      <p>Vorstand: Vorname Name &nbsp;| Vorsitzender des Aufsichtsrats: Vorname Name &nbsp;| Firma AG Sitz Stadt &nbsp;| HRB XXXXX &nbsp;| Amtsgericht in Stadt</p>
      <p>USt-IdNr.: De28956565 | Bankverbindung: &nbsp;Bank xyz | DE97 1234 0000 1000 0000 00 &nbsp;| BIC XXXXXXX</p>
    </div>
  </div>
</section>

<section class="card front" aria-label="Visitenkarte Vorderseite">
  <div class="card-face">
    <div class="brand">
      <span class="brand-dot" style="width:14px;height:14px;"></span>kernwichtel-beispiel.de
    </div>
  </div>
</section>

<section class="card back" aria-label="Visitenkarte Rückseite">
  <div class="card-face">
    <div class="brand">
      <span class="brand-dot" style="width:8px;height:8px;"></span>kernwichtel-beispiel.de
    </div>
    <p class="contact-name">Max Mustermann</p>
    <p class="contact-title">Titel</p>
    <div class="contact-address">
      <p>Musterfirma</p>
      <p>Musterstraße</p>
      <p>12345 Musterhausen</p>
    </div>
    <table class="contact-lines">
      <tr><td>Telefon</td><td>+49 (0) 1234 567890</td></tr>
      <tr><td>Mobil</td><td>&nbsp;&nbsp;&nbsp;&nbsp;+49 (0) 123 4567890</td></tr>
      <tr><td>Fax</td><td>&nbsp;&nbsp;&nbsp;&nbsp;+49 (0) 1234 567891</td></tr>
    </table>
    <p class="contact-mail">info@kernwichtel-beispiel.de</p>
  </div>
</section>

</body>
</html>
```